Postcard design to acquire new clients for my Property Management Company

I'm looking for a postcard design that I can send to prospective clients detailing information about my company and services.
Postcard should be eye catching and contain information from www.brightkeyrentals-example.com. I've provided a few screen shots for the most important information and my logo.
Target Market(s)
Real Estate
Industry/Entity Type
Real Estate
Font styles to use
Sans Serif
Requirements
Must have
- Must be eye catching!! this will be a direct mail piece - I'd like for the card to be read and not tossed in the trash immediately.
Design que from the logo.
A place to write / print the receipts name and address.
our physical address - 2287 Marble Lane, Lubbock, TX 79555.
Should not have
- the contact information on the business card is not accurate - please use info from website.

```html
<!DOCTYPE html>
<html lang="en">
<head>
<meta charset="utf-8">
<title>BrightKey Property Management – Postcard</title>
<link href="https://fonts.googleapis.com/css2?family=Montserrat:wght@400;500;600;700;800&display=swap" rel="stylesheet">
<style>
  :root{
    --navy:#0b4a78;
    --navy-deep:#084874;
    --band-gray:#a3a3a3;
    --icon-gray:#b9c4cf;
    --text-dark:#222;
    --muted:#8a8a8a;
    --card-white:#f4f4f4;
    --back-bg:#ececec;
    --page-bg:#e4e4e4;
    --rule:#9a9a9a;
    --mark-gray:#a6a6a6;
  }
  *{box-sizing:border-box;margin:0;padding:0}
  html,body{width:1200px;height:1200px;overflow:hidden}
  body{background:var(--page-bg);font-family:'Montserrat',sans-serif;position:relative}

  .postcard{position:absolute;left:279px;width:632px;height:421px;overflow:hidden;box-shadow:0 2px 6px rgba(0,0,0,.18)}
  .postcard--front{top:143px;background:var(--card-white)}
  .postcard--back{top:637px;background:var(--back-bg)}

  .front-shapes{position:absolute;left:0;top:0}

  .brand{position:absolute;left:41px;top:34px;color:var(--navy);font-weight:600}
  .brand__name{font-size:31px;letter-spacing:6px;line-height:1}
  .brand__tag{font-size:14.5px;letter-spacing:3.2px;margin-top:6px;font-weight:500}

  .services-band{position:absolute;left:41px;top:109px;color:#fff}
  .services-band__title{font-size:17px;font-weight:700}
  .services-band__sub{font-size:11px;font-weight:400;margin-top:2px;color:#f3f3f3}

  .service-list{position:absolute;left:41px;top:163px;list-style:none}
  .service-list li{display:flex;align-items:center;height:23.8px;color:#fff;font-size:14px;font-weight:500;letter-spacing:.2px}
  .service-list svg{width:18px;height:16px;margin-right:11px;fill:var(--icon-gray)}

  .hero-text{position:absolute;right:25px;top:180px;text-align:right;color:#fff}
  .hero-text__headline{font-size:23.5px;font-weight:800;line-height:29px;text-transform:uppercase}
  .hero-text__sub{font-size:14.5px;font-weight:500;line-height:18.5px;margin-top:7px;white-space:nowrap}

  .contact-bar{position:absolute;left:0;top:365px;width:632px;height:56px;display:flex;align-items:center;padding-left:41px;white-space:nowrap}
  .contact-bar__phone{font-size:15px;font-weight:700;color:var(--navy);letter-spacing:1px}
  .contact-bar__divider{width:2px;height:27px;background:var(--rule);margin:0 10px;flex:none}
  .contact-bar__item{font-size:9.8px;color:var(--text-dark);font-weight:500}
  .contact-bar__item b{color:var(--navy);font-weight:700}

  .back-header{position:absolute;top:24px;left:0;width:100%;text-align:center}
  .back-header__title{font-size:18.5px;font-weight:800;color:var(--navy)}
  .back-header__sub{font-size:11.8px;color:var(--text-dark);font-weight:500;margin-top:1px}

  .plan{position:absolute;width:191px;background:var(--card-white);box-shadow:0 1px 4px rgba(0,0,0,.22);text-align:center;padding-top:14px}
  .plan--lease{left:18px;top:86px;height:198px}
  .plan--full{left:220px;top:70px;height:230px}
  .plan--premium{left:422px;top:88px;height:194px}
  .plan__name{font-size:15px;font-weight:700;color:var(--navy)}
  .plan__tag{font-size:10px;color:var(--muted);margin-top:3px}
  .plan__price{font-size:24px;font-weight:800;color:var(--navy);line-height:26px}
  .plan__basis{font-size:10px;color:var(--muted)}
  .plan__features{list-style:none;margin-top:10px}
  .plan__features li{font-size:10.3px;color:var(--text-dark);font-weight:500;line-height:16px}

  .mailing-area{position:absolute;left:0;top:314px;width:632px;height:107px;background:var(--card-white)}
  .mailing-area__return{position:absolute;left:24px;top:30px;width:104px;color:var(--mark-gray)}
  .mailing-area__brand{font-size:15px;font-weight:800;letter-spacing:.5px}
  .mailing-area__address{font-size:8px;font-weight:500;line-height:11px;margin-top:4px;color:#777}
  .mailing-area__line{position:absolute;left:136px;width:364px;height:1px;background:var(--rule)}
  .mailing-area__stamp{position:absolute;left:536px;top:16px;width:74px;height:74px;border:1px solid #222}
</style>
</head>
<body>

<section class="postcard postcard--front">
  <svg class="front-shapes" width="632" height="421" viewBox="0 0 632 421">
    <defs>
      <linearGradient id="heroTone" x1="0" y1="0" x2="0" y2="1">
        <stop offset="0" stop-color="#3b78ad"/>
        <stop offset=".5" stop-color="#4a5f80"/>
        <stop offset="1" stop-color="#c55a3f"/>
      </linearGradient>
    </defs>
    <polygon role="img" aria-label="Photo of a Lubbock office building at dusk" points="434,0 632,0 632,365 277,365" fill="url(#heroTone)"/>
    <polygon points="0,102 390,102 369,150 0,150" fill="var(--band-gray)"/>
    <polygon points="0,150 369,150 277,365 0,365" fill="var(--navy-deep)"/>
  </svg>

  <div class="brand">
    <div class="brand__name">BRIGHTKEY</div>
    <div class="brand__tag">PROPERTY MANAGEMENT</div>
  </div>

  <div class="services-band">
    <div class="services-band__title">DISCOVER OUR SERVICES</div>
    <div class="services-band__sub">We offer full-service property management solutions</div>
  </div>

  <ul class="service-list">
    <li><svg viewBox="0 0 18 16"><path d="M9 1 1 8h2.5v7h4.2v-4.5h2.6V15h4.2V8H17z"/></svg>PROPERTY MARKETING</li>
    <li><svg viewBox="0 0 18 16"><circle cx="6" cy="5" r="3"/><circle cx="13" cy="5" r="2.6"/><path d="M0 15c0-4 3-6 6-6s6 2 6 6zM12.5 9c3 0 5.5 1.8 5.5 5.5h-5c0-2-.5-4-1.8-5.3z"/></svg>TENANT SCREENING</li>
    <li><svg viewBox="0 0 18 16"><text x="9" y="14" text-anchor="middle" font-size="16" font-weight="700" font-family="Montserrat,sans-serif" fill="var(--icon-gray)">$</text></svg>RENT COLLECTION</li>
    <li><svg viewBox="0 0 18 16"><path d="M9 2h6l2 3-3 1-2-1-8 10-2-2 8-8z"/></svg>MAINTENANCE</li>
    <li><svg viewBox="0 0 18 16"><path d="M7 1a6 6 0 1 0 3.6 10.8L15 16l1.6-1.6-4.3-4.4A6 6 0 0 0 7 1zm0 2.5a3.5 3.5 0 1 1 0 7 3.5 3.5 0 0 1 0-7z"/></svg>PROPERTY INSPECTIONS</li>
    <li><svg viewBox="0 0 18 16"><path d="M1 1h1.3v13H17v1.3H1z"/><rect x="4" y="9" width="1.6" height="4"/><rect x="7" y="6" width="1.6" height="7"/><rect x="10" y="8" width="1.6" height="5"/><rect x="13" y="4" width="1.6" height="9"/></svg>FINANCIAL REPORTING</li>
    <li><svg viewBox="0 0 18 16"><path d="M9 0 2 2.5V7c0 4.2 3 7.6 7 9 4-1.4 7-4.8 7-9V2.5z"/></svg>EVICTIONS</li>
    <li><svg viewBox="0 0 18 16"><path d="M8.3 1h1.4v12H13v1.5H5V13h3.3zM2 4h14v1.2H2zM3 5 .5 10h5zM15 5l-2.5 5h5zM.5 10.5h5a2.5 1.6 0 0 1-5 0zM12.5 10.5h5a2.5 1.6 0 0 1-5 0z"/></svg>LEGAL GUIDANCE</li>
  </ul>

  <div class="hero-text">
    <div class="hero-text__headline">Property<br>Management<br>Across<br>Lubbock, TX</div>
    <div class="hero-text__sub">Maximize your financial returns with<br>support from our rental specialists</div>
  </div>

  <div class="contact-bar">
    <span class="contact-bar__phone">(806) 555-0142</span>
    <span class="contact-bar__divider"></span>
    <span class="contact-bar__item">info@brightkeyrentals-example.com</span>
    <span class="contact-bar__divider"></span>
    <span class="contact-bar__item">www.<b>brightkeyrentals-example</b>.com</span>
  </div>
</section>

<section class="postcard postcard--back">
  <header class="back-header">
    <h1 class="back-header__title">CHOOSE THE RIGHT PROPERTY MANAGEMENT SYSTEM</h1>
    <p class="back-header__sub">Selecting the wrong manager could be your costliest mistake ever.</p>
  </header>

  <article class="plan plan--lease">
    <h2 class="plan__name">Lease Only</h2>
    <p class="plan__tag">- You Just Need Tenants -</p>
    <p class="plan__price">9%</p>
    <p class="plan__basis">of annual lease</p>
    <ul class="plan__features">
      <li>Professional Photography</li>
      <li>Marketing &amp; Advertising</li>
      <li>Property Showings</li>
      <li>Tenant Screening &amp; Qualifications</li>
      <li>Lease Execution</li>
      <li>Move In Coordination</li>
    </ul>
  </article>

  <article class="plan plan--full">
    <h2 class="plan__name">Full Service</h2>
    <p class="plan__tag">- Our Most Popular -</p>
    <p class="plan__price">10%</p>
    <p class="plan__basis">of monthly rent</p>
    <ul class="plan__features">
      <li>Includes Leasing Service</li>
      <li>24/7 Emergency Response</li>
      <li>Move In &amp; Out Inspections</li>
      <li>Professional Lease Enforcement</li>
      <li>Schedule &amp; Oversee all Repairs</li>
      <li>Pay all Invoices</li>
      <li>Monthly &amp; Year End Statements</li>
      <li>Annual Market Rent Analysis</li>
    </ul>
  </article>

  <article class="plan plan--premium">
    <h2 class="plan__name">Premium Service</h2>
    <p class="plan__tag">- Our Premier Service -</p>
    <p class="plan__price">12%</p>
    <p class="plan__basis">of monthly rent</p>
    <ul class="plan__features">
      <li>Includes Full Service Features</li>
      <li>Professional Video Marketing</li>
      <li>Home Warranty Coordination</li>
      <li>Tenant Retention Program</li>
    </ul>
  </article>

  <div class="mailing-area">
    <div class="mailing-area__return">
      <div class="mailing-area__brand">BRIGHTKEY</div>
      <div class="mailing-area__address">2287 Marble Lane<br>Lubbock, TX 79555</div>
    </div>
    <div class="mailing-area__line" style="top:32px"></div>
    <div class="mailing-area__line" style="top:60px"></div>
    <div class="mailing-area__line" style="top:87px"></div>
    <div class="mailing-area__stamp"></div>
  </div>
</section>

</body>
</html>
```